Online Advice via Video Site requires Cutting Edge Homepage

We need a creative new and exciting webdesign for our tutoring via video-chat website.

We have prepared a "demo" homepage for you to see various promotional material that we think would be suitable for the homepage. http://www.quizlanterna.com/demo

The actual site is undergoing some final tinkering but can be accessed and used at http://www.quizlanterna.com

There is NO NEED to take any colours or design structure from this.

We expect the logo to be changed to match the new site. The new logo should match the site's function.

I have included some other projects that we like the look of:
http://www.artflockly.com.au/design/143762
http://www.artflockly.com.au/design/561630
http://www.artflockly.com.au/design/247199
http://www.artflockly.com.au/design/255195
http://www.bravolumo.tv/

Target Market(s)

People that will work as tutors/advisers or be student/clients

Industry/Entity Type

Tutoring

Requirements
Must have
• The search is the main feature of the homepage

After the search the next goal of the page is to get people to sign up to the site

Login, (optional inclusion of the chatterbox login - if you don't include it then you need only have a "login" button... no username or password input fields)

Footer
Nice to have
• The promotional material for the site, the colours on the Slidora file CAN BE changed to suit the new design you propose.

```html
<!DOCTYPE html>
<html lang="en">
<head>
<meta charset="utf-8">
<title>Quiz Lanterna – Instant Personal Advice</title>
<link href="https://fonts.googleapis.com/css2?family=Courgette&family=Arimo:wght@400;700&display=swap" rel="stylesheet">
<style>
:root{
  --crimson:#b0234d;
  --crimson-dark:#8c1a3b;
  --crimson-light:#c93563;
  --magenta:#b0157d;
  --beige:#d6bfb9;
  --beige-light:#f1e6e3;
  --footer:#c5a69e;
  --brand-grey:#6b5d5b;
  --text:#555;
  --muted:#9a9a9a;
  --white:#fff;
  --player:#1f1f1f;
}
*{box-sizing:border-box;margin:0;padding:0}
html,body{width:1200px;height:1193px;overflow:hidden}
body{position:relative;font-family:"Arimo",Arial,sans-serif;color:var(--text);background:var(--white)}
.abs{position:absolute}

/* header */
.header{left:0;top:0;width:1200px;height:590px;
  background:radial-gradient(ellipse 700px 380px at 600px 330px,var(--beige-light) 0%,#e2d0cb 55%,var(--beige) 100%)}
.brand{left:170px;top:50px;display:flex;align-items:center;gap:12px}
.brand-dot{width:24px;height:24px;border-radius:50%;background:var(--crimson)}
.brand-name{font-family:"Courgette",cursive;font-size:42px;color:var(--crimson);line-height:1}

.nav{left:591px;top:0;display:flex}
.nav a{font-family:"Courgette",cursive;color:var(--white);text-decoration:none;font-size:19px;
  height:80px;line-height:104px;padding:0 13px;text-shadow:0 1px 2px rgba(0,0,0,.25)}
.nav a.active{background:linear-gradient(var(--crimson-light),var(--crimson-dark));width:86px;text-align:center;padding:0}

.search{left:591px;top:93px;width:444px;height:37px;display:flex;box-shadow:0 2px 4px rgba(0,0,0,.15)}
.search input{flex:1;border:0;background:var(--white);font:15px "Arimo",sans-serif;padding:0 18px;color:var(--muted)}
.search button{width:88px;border:0;background:linear-gradient(var(--crimson-light),var(--crimson-dark));
  color:var(--white);font:20px "Courgette",cursive}
.login{left:1047px;top:93px;width:70px;height:37px;background:var(--white);color:var(--crimson);
  font:17px "Courgette",cursive;text-align:center;line-height:37px;text-decoration:none;box-shadow:0 2px 4px rgba(0,0,0,.15)}

/* hero */
.hero{left:165px;top:187px;width:872px;height:348px;background:var(--white);box-shadow:0 3px 8px rgba(0,0,0,.25)}
.testimonials{left:0;top:0;width:272px;height:348px}
.tab{position:absolute;left:0;top:0;width:272px;height:36px;background:linear-gradient(var(--crimson-light),var(--crimson-dark));
  color:var(--white);font:19px "Courgette",cursive;padding:5px 14px}
.quote{position:absolute;left:13px;width:246px;display:flex;gap:10px;padding-bottom:12px;border-bottom:1px dotted #ccc}
.quote-1{top:56px}.quote-2{top:138px}.quote-3{top:220px;border:0}
.avatar{width:60px;height:60px;border-radius:50%;background:radial-gradient(#c9a491,#8d6b5c);flex:none;border:2px solid #eee}
.quote h3{font-size:10px;color:var(--crimson);font-weight:700;margin-top:4px;white-space:nowrap}
.quote p{font-size:9.5px;line-height:1.4;color:#666;margin-top:4px}
.quote small{display:block;font-size:8.5px;color:var(--muted);margin-top:5px}
.quote small b{color:var(--crimson)}
.btn-view{position:absolute;left:13px;top:308px;width:59px;height:26px;background:var(--magenta);color:var(--white);
  font:13px "Courgette",cursive;text-align:center;line-height:26px}
.btn-connect{position:absolute;left:125px;top:308px;width:132px;height:26px;background:#3d4f7c;color:var(--white);
  font-size:10px;text-align:center;line-height:26px}

.video{left:272px;top:0;width:600px;height:348px;background:var(--player)}
.video-art{position:absolute;left:0;top:0;width:600px;height:322px;background:linear-gradient(135deg,#4a4a4a,#2e2e2e 60%,#3b3b3b)}
.video-play{position:absolute;left:240px;top:100px}
.video-caption{position:absolute;left:20px;top:262px;width:560px;text-align:center;color:#ddd;font:16px "Courgette",cursive;line-height:1.45}
.video-bar{position:absolute;left:0;bottom:0;width:600px;height:26px;background:#111;color:#ccc;font-size:10px}
.progress{position:absolute;left:0;top:0;width:600px;height:4px;background:var(--crimson)}

/* follow */
.follow{left:1111px;top:317px;width:89px;height:197px;background:var(--white);box-shadow:-2px 2px 6px rgba(0,0,0,.15);padding:6px 0 0 12px}
.follow span{font:14px "Courgette",cursive;color:var(--crimson)}
.social{width:32px;height:32px;margin:8px 0 0 36px;border-radius:3px}

/* content */
.zig{left:0;width:1200px;height:10px}
.zig-top{top:580px;background:linear-gradient(135deg,var(--white) 5px,transparent 5px) 0 0/10px 10px,linear-gradient(225deg,var(--white) 5px,transparent 5px) 0 0/10px 10px}
.zig-bottom{top:995px;background:linear-gradient(45deg,var(--footer) 5px,transparent 5px) 0 0/10px 10px,linear-gradient(-45deg,var(--footer) 5px,transparent 5px) 0 0/10px 10px}
.glow{border-radius:50%}
.glow-yellow{left:350px;top:820px;width:360px;height:360px;background:radial-gradient(#fbf5d8,rgba(255,255,255,0) 70%)}
.glow-pink{left:620px;top:870px;width:330px;height:330px;background:radial-gradient(#f3e0e0,rgba(255,255,255,0) 70%)}
.decor-plant{left:98px;top:958px;width:66px;height:40px;background:linear-gradient(#7c9550,#58703a);opacity:.8}

.welcome{left:185px;top:612px;width:492px}
.welcome h1{font:400 24px "Courgette",cursive;color:var(--crimson)}
.lead{font-size:15px;font-weight:700;color:#6a6a6a;line-height:1.45;margin-top:22px}
.body{font-size:12.5px;color:#aaa;line-height:1.55;margin-top:14px}
.checks{list-style:none;margin-top:26px}
.checks li{font-size:12.5px;font-weight:700;color:#555;display:flex;align-items:center;gap:10px;margin-bottom:6px}
.checks svg{flex:none}

.panel{left:717px;width:302px;background:linear-gradient(var(--crimson-light),var(--crimson-dark));border-radius:3px;color:var(--white);text-align:center;box-shadow:0 2px 6px rgba(0,0,0,.2)}
.panel h2{font-weight:400;font-size:17px;padding:20px 0 12px}
.advice{top:612px;height:159px}
.advice p{font-size:13px;font-weight:700;line-height:1.35;margin-bottom:14px}
.arrow{position:absolute;top:74px}
.blog{top:794px;height:169px}
.blog ul{list-style:none;display:grid;grid-template-columns:140px 110px;text-align:left;margin-left:48px}
.blog li{font-size:13px;font-weight:700;padding:3px 0 5px 0}
.blog li.current{background:rgba(0,0,0,.2);margin-left:-14px;padding-left:14px}

/* footer */
.footer{left:0;top:1003px;width:1200px;height:190px;background:var(--footer)}
.footer-title{font:400 17px "Courgette",cursive;color:var(--crimson-dark)}
.sitemap{left:185px;top:1048px}
.links{display:grid;grid-template-columns:134px 100px;margin-top:12px}
.links a{color:var(--white);font-size:12px;font-weight:700;text-decoration:none;line-height:24px}
.newsletter{left:476px;top:1048px;width:200px}
.newsletter p{font-size:10px;color:var(--white);margin-top:8px}
.newsletter input{width:196px;height:26px;border:0;margin-top:8px;font:italic 11px "Arimo",sans-serif;padding:0 12px;color:#aaa}
.subscribe{margin-top:12px;width:118px;height:28px;border-radius:14px;background:var(--crimson-dark);color:var(--white);
  font:17px "Courgette",cursive;text-align:center;line-height:28px}
.foot-brand{left:735px;top:1085px;display:flex;align-items:center;gap:12px}
.foot-brand .brand-dot{background:var(--brand-grey)}
.foot-brand .brand-name{color:var(--brand-grey);font-size:40px}
.copy{left:755px;top:1172px;font-size:10px;color:var(--white)}
</style>
</head>
<body>
<header class="abs header"></header>

<div class="abs brand"><span class="brand-dot"></span><span class="brand-name">Quiz Lanterna</span></div>

<nav class="abs nav">
  <a class="active" href="#">Home</a><a href="#">About Us</a><a href="#">Contact Us</a><a href="#">Blog</a><a href="#">News</a>
</nav>

<form class="abs search"><input type="text" value="Search Quiz Lanterna's Topic &amp; Advisors"><button type="button">Search</button></form>
<a class="abs login" href="#">Login</a>

<section class="abs hero">
  <div class="abs testimonials">
    <div class="tab">Testimonial</div>
    <article class="quote quote-1"><div class="avatar" role="img" aria-label="Portrait of Rita"></div>
      <div><h3>Testimonial headline gose here..</h3><p>Lorem Ipsum is simply dummy text of the printing and typesetting industry...</p><small>Publish by : <b>Rita</b>, 22 Feb, 2012</small></div></article>
    <article class="quote quote-2"><div class="avatar" role="img" aria-label="Portrait of Nicole"></div>
      <div><h3>Testimonial headline gose here..</h3><p>Lorem Ipsum is simply dummy text of the printing and typesetting industry...</p><small>Publish by : <b>Nicole</b>, 22 Feb, 2012</small></div></article>
    <article class="quote quote-3"><div class="avatar" role="img" aria-label="Portrait of Rita"></div>
      <div><h3>Testimonial headline gose here..</h3><p>Lorem Ipsum is simply dummy text of the printing and typesetting industry...</p><small>Publish by : <b>Rita</b>, 22 Feb, 2012</small></div></article>
    <a class="btn-view">View all</a>
    <a class="btn-connect">Connect using Chatterbox</a>
  </div>
  <div class="abs video">
    <div class="video-art" role="img" aria-label="Promotional video still: a mosaic of many expert portraits"></div>
    <svg class="video-play" width="120" height="120" viewBox="0 0 120 120"><circle cx="60" cy="60" r="54" fill="rgba(255,255,255,.12)" stroke="rgba(255,255,255,.6)" stroke-width="6"/><path d="M48 38 L84 60 L48 82Z" fill="rgba(255,255,255,.7)"/></svg>
    <p class="video-caption">Imagine if, whenever you had a problem you could instantly access the world's experts to solve it. Now you can!</p>
    <div class="video-bar"><div class="progress"></div>
      <svg class="abs" style="left:14px;top:9px" width="70" height="14"><path d="M0 0L10 6L0 12Z" fill="#ccc"/><path d="M36 4h4l5-4v12l-5-4h-4z" fill="#ccc"/></svg>
      <span class="abs" style="left:88px;top:9px">0:00</span>
      <span class="abs" style="left:510px;top:8px;width:40px;height:10px;background:#444"></span>
      <svg class="abs" style="left:568px;top:8px" width="14" height="12"><path d="M0 4V0h4M10 0h4v4M14 8v4h-4M4 12H0V8" stroke="#ccc" fill="none" stroke-width="1.5"/></svg>
    </div>
  </div>
</section>

<aside class="abs follow"><span>Follow us</span>
  <div class="social" style="background:#3d5a98"></div><div class="social" style="background:#55acee"></div>
  <div class="social" style="background:#c4302b"></div><div class="social" style="background:#e8772e"></div>
</aside>

<div class="abs zig zig-top"></div>
<div class="abs glow glow-yellow"></div>
<div class="abs glow glow-pink"></div>
<div class="abs decor-plant" role="img" aria-label="Small decorative plant illustration"></div>

<section class="abs welcome">
  <h1>Wellcome to Quiz Lanterna</h1>
  <p class="lead">"Imagine if, whenever you had a problem you could instantly access the world's experts to solve it. Now you can!"</p>
  <p class="body">Lorem ipsum dolor sit amet, consectetur adipiscing elit. Aliquam eu ligula vitae eros molestie mollis. Nunc feugiat velit sed sem tempus et faucibus nunc adipiscing. Aliquam tristique urna quis ligula imperdiet a volutpat quam condimentum. Lorem ipsum dolor sit amet, consectetur adipiscing elit. Aliquam eu ligula vitae eros molestie mollis. Nunc feugiat velit sed sem tempus et faucibus nunc adipiscing. Aliquam tristique urna quis ligula imperdiet a volutpat quam condimentum.</p>
  <ul class="checks">
    <li><svg width="12" height="12"><rect width="12" height="12" fill="var(--crimson)"/><path d="M3 6l2 2 4-5" stroke="#fff" stroke-width="1.6" fill="none"/></svg>QuizLanterna is the place for e-learning, mentoring &amp; professional advice</li>
    <li><svg width="12" height="12"><rect width="12" height="12" fill="var(--crimson)"/><path d="M3 6l2 2 4-5" stroke="#fff" stroke-width="1.6" fill="none"/></svg>It instantly connects people with knowledge and those who need it</li>
    <li><svg width="12" height="12"><rect width="12" height="12" fill="var(--crimson)"/><path d="M3 6l2 2 4-5" stroke="#fff" stroke-width="1.6" fill="none"/></svg>Connects people for ongoing advice or on off answers</li>
    <li><svg width="12" height="12"><rect width="12" height="12" fill="var(--crimson)"/><path d="M3 6l2 2 4-5" stroke="#fff" stroke-width="1.6" fill="none"/></svg>Ask questions and/or work exactly when it suits you</li>
  </ul>
</section>

<section class="abs panel advice">
  <h2>Instant Personal Advice</h2>
  <p>Advisors - Enter your:<br>Topic, buget, availability</p>
  <p>Clients - SEARCH now<br>Compare ratea, rating &amp; resumes</p>
  <svg class="arrow" style="left:6px" width="22" height="22"><circle cx="11" cy="11" r="11" fill="#2a1018"/><path d="M13 6l-5 5 5 5" stroke="#fff" stroke-width="2" fill="none"/></svg>
  <svg class="arrow" style="right:6px" width="22" height="22"><circle cx="11" cy="11" r="11" fill="#2a1018"/><path d="M9 6l5 5-5 5" stroke="#fff" stroke-width="2" fill="none"/></svg>
</section>

<section class="abs panel blog">
  <h2>Recent Blog Post</h2>
  <ul><li>English</li><li>Agriculture</li><li class="current">Building</li><li>Veterinary</li><li>Cultural studies</li><li>Science</li><li>Criminology</li><li>Building</li></ul>
</section>

<footer class="abs footer"></footer>
<div class="abs zig zig-bottom"></div>

<div class="abs sitemap"><h4 class="footer-title">Site Map</h4>
  <div class="links"><a href="#">About us</a><a href="#">Blog</a><a href="#">Student</a><a href="#">FAQs</a><a href="#">Advisors</a><a href="#">Our Technology</a><a href="#">Topics</a><a href="#">Contact</a></div>
</div>

<div class="abs newsletter"><h4 class="footer-title">Monthly Newsletter</h4>
  <p>Subscribe Now for free news letter</p>
  <input type="email" value="Email Address">
  <div class="subscribe">Subscribe</div>
</div>

<div class="abs foot-brand"><span class="brand-dot"></span><span class="brand-name">Quiz Lanterna</span></div>
<p class="abs copy">Copyrights © QuizLanterna 2012</p>
</body>
</html>
```